Soap/cosmetic labels

Need labels that incorporate my brand , to fit onto rectangular and round labels readable down to two inches. Key ideas are luxury, nourishing, handmade, palm oil/paraben free, cruelty free, savon artisanal. One line will be called The Tender Cake by The Dune Wanderer with key words: fragrance free, all natural colorants. The other line is luxury oils, fragrance, indulgent and just The Dune Wanderer

Target Market(s)

Women mostly

Industry/Entity Type

cosmetics/soap

Colors
0094D4
00A9DD
6FCCEA
C7EBF8
E9F6FB

Requirements
Must have
• place for me to change fragrance and cosmetic type; gold goes on black labels; blue on white labels
Nice to have
• fit the brand

```html
<!DOCTYPE html>
<html lang="en">
<head>
<meta charset="utf-8">
<title>The Tender Cake – Label Set</title>
<link href="https://fonts.googleapis.com/css2?family=Josefin+Sans:wght@300;400&family=Kanit:wght@700&family=Exo+2:wght@600&display=swap" rel="stylesheet">
<style>
  :root {
    --backdrop: #adc9d1;
    --black: #000000;
    --gold: #e3af43;
    --white: #ffffff;
    --blue: #00a9dd;
    --ink: #111111;
  }
  * { margin: 0; padding: 0; box-sizing: border-box; }
  html, body { width: 1200px; height: 1200px; overflow: hidden; }
  body { background: var(--backdrop); position: relative; }

  .label {
    position: absolute;
    width: 415px;
    height: 415px;
    overflow: hidden;
    box-shadow: 0 6px 14px rgba(40, 70, 80, 0.45);
  }
  .label--square { border-radius: 18px; }
  .label--round { border-radius: 50%; }
  .label--col1 { left: 159px; }
  .label--col2 { left: 625px; }
  .label--row1 { top: 159px; }
  .label--row2 { top: 626px; }

  .theme-gold { background: var(--black); --accent: var(--gold); --byline: var(--white); --band-text: var(--ink); }
  .theme-blue { background: var(--white); --accent: var(--blue); --byline: var(--ink); --band-text: var(--white); }

  .brand {
    position: absolute;
    display: flex;
    align-items: center;
    color: var(--accent);
    font-family: "Josefin Sans", sans-serif;
    font-weight: 400;
    white-space: nowrap;
  }
  .brand__dot { border-radius: 50%; background: var(--accent); flex: none; }
  .label--square .brand { left: 52px; top: 52px; font-size: 27px; gap: 14px; }
  .label--square .brand__dot { width: 67px; height: 67px; }
  .label--round .brand { left: 84px; top: 65px; font-size: 22px; gap: 12px; }
  .label--round .brand__dot { width: 52px; height: 52px; }

  .band {
    position: absolute;
    left: 0; right: 0; bottom: 0;
    top: 333px;
    background: var(--accent);
  }

  .figure-art {
    position: absolute;
    left: 0;
    background: var(--accent);
    border-radius: 0 75% 20% 0 / 0 45% 55% 0;
  }
  .label--square .figure-art { top: 171px; width: 143px; height: 226px; }
  .label--round .figure-art { top: 177px; width: 143px; height: 220px; }

  .product {
    position: absolute;
    color: var(--accent);
    font-family: "Kanit", sans-serif;
    font-weight: 700;
    font-size: 30px;
    line-height: 32px;
    letter-spacing: 1.5px;
  }
  .label--square .product { left: 154px; top: 222px; }
  .label--round .product { left: 152px; top: 210px; }

  .byline {
    display: block;
    margin-top: 4px;
    color: var(--byline);
    font-family: "Josefin Sans", sans-serif;
    font-weight: 300;
    font-size: 14px;
    line-height: 16px;
    letter-spacing: 2px;
  }

  .keywords {
    position: absolute;
    color: var(--band-text);
    font-family: "Exo 2", sans-serif;
    font-weight: 600;
    text-transform: uppercase;
    letter-spacing: 1.2px;
  }
  .label--square .keywords { left: 115px; top: 346px; font-size: 13px; line-height: 18.5px; }
  .label--round .keywords { left: 0; right: 0; top: 347px; text-align: center; font-size: 10.5px; line-height: 13.5px; }
</style>
</head>
<body>

  <div class="label label--square label--col1 label--row1 theme-gold">
    <div class="brand"><span class="brand__dot"></span>The Dune Wanderer</div>
    <div class="band"></div>
    <div class="figure-art" role="img" aria-label="Gold silhouette illustration of a woman with flowing hair"></div>
    <h1 class="product">THE<br>TENDER CAKE<span class="byline">BY THE DUNE WANDERER</span></h1>
    <p class="keywords">Luxury, nourishing, handmade,<br>paraben free, cruelty free,<br>savon artisanal</p>
  </div>

  <div class="label label--round label--col2 label--row1 theme-gold">
    <div class="brand"><span class="brand__dot"></span>The Dune Wanderer</div>
    <div class="band"></div>
    <div class="figure-art" role="img" aria-label="Gold silhouette illustration of a woman with flowing hair"></div>
    <h2 class="product">THE<br>TENDER CAKE<span class="byline">BY THE DUNE WANDERER</span></h2>
    <p class="keywords">Luxury, nourishing, handmade,<br>paraben free, cruelty free,<br>savon artisanal</p>
  </div>

  <div class="label label--square label--col1 label--row2 theme-blue">
    <div class="brand"><span class="brand__dot"></span>The Dune Wanderer</div>
    <div class="band"></div>
    <div class="figure-art" role="img" aria-label="Blue silhouette illustration of a woman with flowing hair"></div>
    <h2 class="product">THE<br>TENDER CAKE<span class="byline">BY THE DUNE WANDERER</span></h2>
    <p class="keywords">Luxury, nourishing, handmade,<br>paraben free, cruelty free,<br>savon artisanal</p>
  </div>

  <div class="label label--round label--col2 label--row2 theme-blue">
    <div class="brand"><span class="brand__dot"></span>The Dune Wanderer</div>
    <div class="band"></div>
    <div class="figure-art" role="img" aria-label="Blue silhouette illustration of a woman with flowing hair"></div>
    <h2 class="product">THE<br>TENDER CAKE<span class="byline">BY THE DUNE WANDERER</span></h2>
    <p class="keywords">Luxury, nourishing, handmade,<br>paraben free, cruelty free,<br>savon artisanal</p>
  </div>

</body>
</html>
```